starting a new business venture, need business cards and website friendly Logo. Professional, Classy, Unique!
(Need Creative)

Business Name:
BRAXMOREN Coaching and Capital Group

4193 Kestrel Bend Rd. Box 518
Harwick, Vermont 43952
614-582-7309

www.braxmoren.com

Quote: Try and Fail but NEVER Fail to Try

```html
<!DOCTYPE html>
<html lang="en">
<head>
<meta charset="utf-8">
<title>BRAXMOREN Coaching and Capital Group – Business Card</title>
<link rel="stylesheet" href="https://fonts.googleapis.com/css2?family=Open+Sans:wght@400;600;700&display=swap">
<style>
  :root {
    --navy: #2e2f86;
    --navy-light: #3c46a0;
    --white: #ffffff;
    --yellow: #f7c21b;
    --charcoal: #3a3a3c;
    --ink: #1f1f24;
    --backdrop: #232325;
  }
  * { margin: 0; padding: 0; box-sizing: border-box; }
  html, body { width: 1200px; height: 900px; overflow: hidden; }
  body {
    background: var(--backdrop);
    font-family: "Open Sans", Arial, sans-serif;
    position: relative;
  }
  .card {
    position: absolute;
    left: 260px;
    width: 680px;
    height: 389px;
    background: var(--white);
    overflow: hidden;
  }
  .card--front { top: 38px; }
  .card--back { top: 472px; }
  .card__shapes { position: absolute; inset: 0; width: 100%; height: 100%; }

  .brand-mark {
    position: absolute;
    left: 50%; top: 150px;
    transform: translateX(-50%);
    display: flex; align-items: center; gap: 12px;
    white-space: nowrap;
  }
  .brand-mark__square {
    width: 34px; height: 34px;
    background: var(--yellow);
  }
  .brand-mark__name {
    font-weight: 700; font-size: 34px; letter-spacing: 1px;
    color: var(--navy);
  }

  .identity {
    position: absolute; left: 36px; top: 168px;
    display: flex; align-items: center; gap: 10px;
    white-space: nowrap;
  }
  .identity__square { width: 30px; height: 30px; background: var(--yellow); }
  .identity__name {
    font-weight: 600; font-size: 26px; line-height: 1; color: var(--navy);
    letter-spacing: 0.5px;
  }
  .identity__tagline {
    font-size: 13px; color: var(--navy); margin-top: 3px; letter-spacing: 0.3px;
  }

  .contact-strip {
    position: absolute; left: 42px; top: 228px;
    width: 20px; height: 112px;
    background: var(--yellow);
  }
  .contact-list {
    position: absolute; left: 42px; top: 232px;
    list-style: none;
    white-space: nowrap;
  }
  .contact-list__item {
    display: flex; align-items: flex-start; gap: 10px;
    font-size: 12.5px; font-weight: 600; color: var(--ink);
    line-height: 1.3;
    margin-bottom: 16px;
  }
  .contact-list__icon { width: 20px; height: 20px; flex: none; }
</style>
</head>
<body>

  <section class="card card--front" aria-label="Card front">
    <svg class="card__shapes" viewBox="0 0 680 389" preserveAspectRatio="none">
      <path d="M0,0 H360 C250,40 130,150 0,280 Z" fill="var(--navy)"/>
      <path d="M0,312 H680 V389 H0 Z" fill="var(--charcoal)"/>
    </svg>
    <div class="brand-mark">
      <span class="brand-mark__square"></span>
      <span class="brand-mark__name">BRAXMOREN</span>
    </div>
  </section>

  <section class="card card--back" aria-label="Card back">
    <svg class="card__shapes" viewBox="0 0 680 389" preserveAspectRatio="none">
      <path d="M0,0 H680 V40 C580,60 500,40 420,80 C330,125 230,160 0,152 Z" fill="var(--navy)"/>
      <path d="M0,350 C200,360 320,320 420,240 C510,170 590,125 680,118 V389 H0 Z" fill="var(--navy-light)"/>
    </svg>

    <div class="identity">
      <span class="identity__square"></span>
      <div>
        <div class="identity__name">BRAXMOREN</div>
        <div class="identity__tagline">Coaching and Capital Group</div>
      </div>
    </div>

    <div class="contact-strip"></div>
    <ul class="contact-list">
      <li class="contact-list__item">
        <svg class="contact-list__icon" viewBox="0 0 20 20"><circle cx="10" cy="10" r="9" fill="var(--navy)"/><path d="M7 5.5l1.6 2.2-1 1.1c.7 1.4 1.6 2.3 3 3l1.1-1 2.2 1.6-.9 1.6c-3.6-.3-6.8-3.5-7.1-7.1z" fill="#fff"/></svg>
        <span>+614-582-7309</span>
      </li>
      <li class="contact-list__item">
        <svg class="contact-list__icon" viewBox="0 0 20 20"><circle cx="10" cy="10" r="9" fill="var(--navy)"/><circle cx="10" cy="10" r="5" fill="none" stroke="#fff" stroke-width="1.2"/><path d="M5 10h10M10 5c-2 3-2 7 0 10M10 5c2 3 2 7 0 10" fill="none" stroke="#fff" stroke-width="1"/></svg>
        <span>www.braxmoren.com</span>
      </li>
      <li class="contact-list__item">
        <svg class="contact-list__icon" viewBox="0 0 20 20"><circle cx="10" cy="10" r="9" fill="var(--navy)"/><path d="M10 4.5a3.5 3.5 0 0 1 3.5 3.5c0 2.6-3.5 7-3.5 7s-3.5-4.4-3.5-7A3.5 3.5 0 0 1 10 4.5z" fill="#fff"/><circle cx="10" cy="8" r="1.3" fill="var(--navy)"/></svg>
        <span>4193 Kestrel Bend Rd. Box 518<br>Harwick, Vermont 43952</span>
      </li>
    </ul>
  </section>

</body>
</html>
```